Tertulia Bean and Table needs a food menu.

We need a menu design for a small coffeeshop in San Pedro Sula Honduras. We serve bistro style food. It should look clean, eye pleasing, modern and organic.
We are all about the home made feel. Superb quality, only natural ingredients, everything is made from scratch. We serve soups, sandwiches, salads, we specialize in desserts and gelato. We are located inside a hotel, we have both english and spanish speaking customers.

Target Market(s)

Young adults

Industry/Entity Type

Restaurant

Contact Information for Business Card

Tertulia
info@velarocafe-mail.com
Hotel Pinecrest Lodge Suites, San Pedro Sula Honduras
+50497260831

Font styles to use
Sans Serif

Colors

Designer to choose colors to be used in the design.

Requirements
Must have
• elegant and clean feel.
Nice to have
• lettering.

```html
<!DOCTYPE html>
<html lang="en">
<head>
<meta charset="utf-8">
<title>Tertulia Bean and Table — Menu</title>
<link rel="stylesheet" href="https://fonts.googleapis.com/css2?family=Playfair+Display:wght@400;700&family=Montserrat:wght@400;600;700&display=swap">
<style>
  :root {
    --paper: #f8f4ea;
    --brown: #9c7456;
    --brown-soft: #a98369;
    --olive: #9a7c44;
    --ink: #2e2420;
    --frame: #3b2e28;
    --text: #8a6a53;
    --band-text: #fbf4ea;
  }
  * { margin: 0; padding: 0; box-sizing: border-box; }
  html, body { width: 974px; height: 1200px; overflow: hidden; background: var(--paper); }
  .menu { position: relative; width: 974px; height: 1200px; background: var(--paper); font-family: "Montserrat", sans-serif; color: var(--text); }
  .abs { position: absolute; }

  .frame { border: 1.5px solid var(--frame); border-bottom: none; }
  .frame--outer { left: 45px; top: 45px; width: 884px; height: 1060px; }
  .frame--inner { left: 56px; top: 56px; width: 862px; height: 1050px; border-width: 1px; }

  .ornament { background: rgba(156,116,86,.28); border-radius: 40% 10% 40% 10%; }
  .sketch { background: rgba(156,116,86,.12); border-radius: 50%; }

  .brand { left: 0; width: 974px; top: 92px; text-align: center; }
  .brand__name { font-family: "Playfair Display", serif; font-weight: 700; font-size: 92px; line-height: 1; color: var(--ink); letter-spacing: 1px; }
  .brand__tagline { margin-top: 20px; font-family: "Montserrat", sans-serif; font-weight: 600; font-size: 13px; letter-spacing: 5px; text-transform: uppercase; color: var(--text); }
  .brand__rule { left: 291px; top: 268px; width: 394px; }

  .band { background: var(--brown); color: var(--band-text); font-family: "Playfair Display", serif; font-weight: 700; text-align: center; }
  .band--soups { left: 324px; top: 329px; width: 325px; height: 44px; font-size: 24px; line-height: 44px; }

  .dish { width: 236px; }
  .dish__head { display: flex; justify-content: space-between; align-items: baseline; }
  .dish__name { font-weight: 700; font-size: 16px; color: var(--brown); }
  .dish__price { font-size: 21px; color: var(--brown); }
  .dish__rule { width: 36px; height: 1px; background: var(--brown); margin: 8px 0 12px; }
  .dish__desc { font-size: 8.6px; line-height: 1.35; }

  .divider { left: 117px; top: 590px; width: 741px; border-top: 1px dashed var(--brown-soft); }

  .list { left: 98px; width: 281px; }
  .list__title { border-top: 1px solid var(--brown-soft); border-bottom: 1px solid var(--brown-soft); text-align: center; font-family: "Playfair Display", serif; font-weight: 700; font-size: 22px; color: var(--brown); height: 31px; line-height: 30px; }
  .list__items { list-style: none; margin-top: 20px; }
  .list__item { display: flex; align-items: center; height: 24.2px; font-size: 15px; }
  .list__leader { flex: 0 0 112px; margin: 0 16px 0 12px; border-bottom: 1.5px dotted var(--brown-soft); height: 1px; }
  .list__price { margin-left: auto; }

  .sweets { left: 424px; top: 631px; width: 457px; height: 373px; border: 1px solid var(--brown-soft); border-radius: 0 0 8px 8px; }
  .sweets__band { left: -1px; top: -1px; width: 459px; height: 44px; line-height: 44px; font-size: 22px; border-radius: 8px 8px 0 0; }
  .treat { width: 200px; text-align: center; }
  .treat__name { font-weight: 700; font-size: 18px; color: var(--olive); }
  .treat__desc { font-size: 7.6px; line-height: 1.35; margin-top: 3px; }
  .treat__price { margin-top: 7px; font-size: 11px; font-weight: 700; color: var(--olive); letter-spacing: 1px; }
  .treat__dots { letter-spacing: 2px; font-weight: 400; }

  .band--hours { left: 263px; top: 1045px; width: 447px; height: 41px; line-height: 41px; font-family: "Montserrat", sans-serif; font-size: 20px; }

  .beans { left: 0; top: 1070px; width: 974px; height: 130px; background: linear-gradient(to bottom, rgba(248,244,234,0) 0%, #5b3a2a 35%, #2f1f18 70%, #4a2f22 100%); }
</style>
</head>
<body>
<main class="menu">
  <div class="abs frame frame--outer"></div>
  <div class="abs frame frame--inner"></div>

  <div class="abs ornament" style="left:61px;top:62px;width:80px;height:72px" role="img" aria-label="Scroll ornament in the top left corner"></div>
  <div class="abs ornament" style="left:833px;top:62px;width:80px;height:72px" role="img" aria-label="Scroll ornament in the top right corner"></div>
  <div class="abs sketch" style="left:61px;top:175px;width:141px;height:142px" role="img" aria-label="Sketch of falling coffee beans"></div>
  <div class="abs sketch" style="left:865px;top:131px;width:109px;height:251px;border-radius:40% 0 0 40%" role="img" aria-label="Sketch of coffee cups"></div>

  <header class="abs brand">
    <h1 class="brand__name">Tertulia</h1>
    <p class="brand__tagline">bistro · san pedro sula</p>
  </header>
  <svg class="abs brand__rule" width="394" height="20" viewBox="0 0 394 20">
    <line x1="0" y1="10" x2="394" y2="10" stroke="#9c7456" stroke-width="1.5"/>
    <circle cx="197" cy="10" r="8" fill="#f8f4ea" stroke="#9c7456" stroke-width="2"/>
    <circle cx="197" cy="10" r="3" fill="#9c7456"/>
  </svg>

  <h2 class="abs band band--soups">SOUPS</h2>

  <section class="soups">
    <article class="abs dish" style="left:98px;top:402px"><div class="dish__head"><span class="dish__name">LOREM IPSUM</span><span class="dish__price">$10</span></div><div class="dish__rule"></div><p class="dish__desc">Lorem ipsum dolor sit amet, ea eum tation aperiri numquam. Te laboramus cotidieque per.</p></article>
    <article class="abs dish" style="left:371px;top:402px"><div class="dish__head"><span class="dish__name">LOREM IPSUM</span><span class="dish__price">$10</span></div><div class="dish__rule"></div><p class="dish__desc">Lorem ipsum dolor sit amet, ea eum tation aperiri numquam. Te laboramus cotidieque per.</p></article>
    <article class="abs dish" style="left:643px;top:402px"><div class="dish__head"><span class="dish__name">LOREM IPSUM</span><span class="dish__price">$10</span></div><div class="dish__rule"></div><p class="dish__desc">Lorem ipsum dolor sit amet, ea eum tation aperiri numquam. Te laboramus cotidieque per.</p></article>
    <article class="abs dish" style="left:98px;top:488px"><div class="dish__head"><span class="dish__name">LOREM IPSUM</span><span class="dish__price">$10</span></div><div class="dish__rule"></div><p class="dish__desc">Lorem ipsum dolor sit amet, ea eum tation aperiri numquam. Te laboramus cotidieque per.</p></article>
    <article class="abs dish" style="left:371px;top:488px"><div class="dish__head"><span class="dish__name">LOREM IPSUM</span><span class="dish__price">$10</span></div><div class="dish__rule"></div><p class="dish__desc">Lorem ipsum dolor sit amet, ea eum tation aperiri numquam. Te laboramus cotidieque per.</p></article>
    <article class="abs dish" style="left:643px;top:488px"><div class="dish__head"><span class="dish__name">LOREM IPSUM</span><span class="dish__price">$10</span></div><div class="dish__rule"></div><p class="dish__desc">Lorem ipsum dolor sit amet, ea eum tation aperiri numquam. Te laboramus cotidieque per.</p></article>
  </section>

  <div class="abs divider"></div>

  <section class="abs list" style="top:637px">
    <h2 class="list__title">SANDWICHES</h2>
    <ul class="list__items">
      <li class="list__item">LOREM IPSUM<span class="list__leader"></span><span class="list__price">$15</span></li>
      <li class="list__item">LOREM IPSUM<span class="list__leader"></span><span class="list__price">$15</span></li>
      <li class="list__item">LOREM IPSUM<span class="list__leader"></span><span class="list__price">$15</span></li>
      <li class="list__item">LOREM IPSUM<span class="list__leader"></span><span class="list__price">$15</span></li>
      <li class="list__item">LOREM IPSUM<span class="list__leader"></span><span class="list__price">$15</span></li>
    </ul>
  </section>

  <section class="abs list" style="top:835px">
    <h2 class="list__title">SALADS</h2>
    <ul class="list__items">
      <li class="list__item">LOREM IPSUM<span class="list__leader"></span><span class="list__price">$15</span></li>
      <li class="list__item">LOREM IPSUM<span class="list__leader"></span><span class="list__price">$15</span></li>
      <li class="list__item">LOREM IPSUM<span class="list__leader"></span><span class="list__price">$15</span></li>
      <li class="list__item">LOREM IPSUM<span class="list__leader"></span><span class="list__price">$15</span></li>
      <li class="list__item">LOREM IPSUM<span class="list__leader"></span><span class="list__price">$15</span></li>
    </ul>
  </section>

  <section class="abs sweets">
    <h2 class="abs band sweets__band">DESSERTS AND GELATO</h2>
    <article class="abs treat" style="left:19px;top:64px"><h3 class="treat__name">LOREM IPSUM</h3><p class="treat__desc">Lorem ipsum dolor sit amet, ea eum tation aperiri numquam. Te laboramus cotidieque per.</p><p class="treat__price"><span class="treat__dots">·········</span> $15 <span class="treat__dots">·········</span></p></article>
    <article class="abs treat" style="left:239px;top:64px"><h3 class="treat__name">LOREM IPSUM</h3><p class="treat__desc">Lorem ipsum dolor sit amet, ea eum tation aperiri numquam. Te laboramus cotidieque per.</p><p class="treat__price"><span class="treat__dots">·········</span> $15 <span class="treat__dots">·········</span></p></article>
    <article class="abs treat" style="left:19px;top:170px"><h3 class="treat__name">LOREM IPSUM</h3><p class="treat__desc">Lorem ipsum dolor sit amet, ea eum tation aperiri numquam. Te laboramus cotidieque per.</p><p class="treat__price"><span class="treat__dots">·········</span> $15 <span class="treat__dots">·········</span></p></article>
    <article class="abs treat" style="left:239px;top:170px"><h3 class="treat__name">LOREM IPSUM</h3><p class="treat__desc">Lorem ipsum dolor sit amet, ea eum tation aperiri numquam. Te laboramus cotidieque per.</p><p class="treat__price"><span class="treat__dots">·········</span> $15 <span class="treat__dots">·········</span></p></article>
    <article class="abs treat" style="left:19px;top:279px"><h3 class="treat__name">LOREM IPSUM</h3><p class="treat__desc">Lorem ipsum dolor sit amet, ea eum tation aperiri numquam. Te laboramus cotidieque per.</p><p class="treat__price"><span class="treat__dots">·········</span> $15 <span class="treat__dots">·········</span></p></article>
    <article class="abs treat" style="left:239px;top:279px"><h3 class="treat__name">LOREM IPSUM</h3><p class="treat__desc">Lorem ipsum dolor sit amet, ea eum tation aperiri numquam. Te laboramus cotidieque per.</p><p class="treat__price"><span class="treat__dots">·········</span> $15 <span class="treat__dots">·········</span></p></article>
  </section>

  <div class="abs beans" role="img" aria-label="Photograph of roasted coffee beans scattered along the bottom edge"></div>
  <p class="abs band band--hours">DAILY OPEN AT 10AM. TO 10PM.</p>
</main>
</body>
</html>
```